Business card design for BrandVexa
BrandVexa
Project: Business card design for BrandVexa
Business card design for BrandVexa - Printing
Creative Brief
Professional
Dalton Wexford
Edmonton, Alberta, Canada
dalton@brandvexa.example
www.brandvexa.example
Possibly a dark background with nice effects. I am open to layer effect changes of my logo "BV". I will be changing my website banner in the future as well to make everything uniform.
Logo and web address logo can be downloaded here: https://www.filedrop.example/s/q8271n904tbpe3x/BV%20logo%20red%20and%20black.psd
brandvexa brandvexa
I like the bak of draft 44
I believe the"BV" box in the logo should be removed on the front of the cards. It just doesn't look right with the arched themed designs. I do like just the "BV" on the back of the card with url. I was hoping for more effects in the colour rather than just solid. Less red and more grey fading into lighter greys. Hopes this makes sense. Thanks for your hard work!

```html
<!DOCTYPE html>
<html lang="en">
<head>
<meta charset="utf-8">
<title>BrandVexa Business Card</title>
<link rel="stylesheet" href="https://fonts.googleapis.com/css2?family=Arimo:wght@400;700&display=swap">
<style>
:root{
  --page-bg:#e4e1dc;
  --card-top:#3b3b3d;
  --card-bottom:#1c1c1d;
  --glow:rgba(255,255,255,0.32);
  --brand-red:#e0203f;
  --text-light:#f2f2f2;
  --text-muted:#d6d6d6;
  --logo-grey:#c9c9cb;
}
*{margin:0;padding:0;box-sizing:border-box}
html,body{width:1200px;height:993px;overflow:hidden;background:var(--page-bg)}
body{position:relative;font-family:"Arimo",Arial,sans-serif}
.card{
  position:absolute;top:42px;width:510px;height:889px;border-radius:38px;overflow:hidden;
  background:linear-gradient(180deg,var(--card-top) 0%,#2a2a2b 45%,var(--card-bottom) 100%);
  box-shadow:0 6px 18px rgba(0,0,0,0.25);
}
.card-front{left:40px}
.card-back{left:637px}
.front-glow{
  position:absolute;left:-60px;top:-40px;width:640px;height:520px;
  background:radial-gradient(ellipse at 60% 52%,var(--glow) 0%,rgba(255,255,255,0.08) 40%,rgba(255,255,255,0) 70%);
}
.logo{position:absolute;left:51px;top:190px}
.logo-name{font-weight:400;font-size:64px;letter-spacing:3px;line-height:1;color:var(--logo-grey)}
.holder-name{position:absolute;left:72px;top:553px;font-size:42px;font-weight:700;color:var(--brand-red)}
.holder-location{position:absolute;left:72px;top:620px;font-size:26px;font-weight:700;color:var(--text-light)}
.contact-list{position:absolute;left:70px;top:674px;list-style:none}
.contact-list li{display:flex;align-items:center;gap:14px;height:31.5px;font-size:22px;color:var(--text-muted)}
.contact-list svg{width:22px;height:22px;flex:none;fill:var(--text-muted)}
.back-glow{
  position:absolute;left:-20px;top:-60px;width:550px;height:460px;
  background:radial-gradient(ellipse at 50% 40%,rgba(255,255,255,0.18) 0%,rgba(255,255,255,0) 65%);
}
.url-band{
  position:absolute;left:0;right:0;top:773px;height:42px;background:var(--brand-red);
  display:flex;align-items:center;justify-content:center;
  font-weight:700;font-size:28px;color:#fff;
}
</style>
</head>
<body>
<section class="card card-front">
  <div class="front-glow"></div>
  <div class="logo"><span class="logo-name">BrandVexa</span></div>
  <h1 class="holder-name">Dalton Wexford</h1>
  <p class="holder-location">Edmonton, Alberta, Canada</p>
  <ul class="contact-list">
    <li><svg viewBox="0 0 24 24"><path d="M12 2a10 10 0 1 0 0 20 10 10 0 0 0 0-20zm6.9 6h-3a15 15 0 0 0-1.3-3.9A8 8 0 0 1 18.9 8zM12 4.1c.8 1.1 1.5 2.4 1.9 3.9h-3.8c.4-1.5 1.1-2.8 1.9-3.9zM4.3 14a8 8 0 0 1 0-4h3.4a16 16 0 0 0 0 4zm.8 2h3a15 15 0 0 0 1.3 3.9A8 8 0 0 1 5.1 16zm3-8h-3a8 8 0 0 1 4.3-3.9A15 15 0 0 0 8.1 8zM12 19.9c-.8-1.1-1.5-2.4-1.9-3.9h3.8c-.4 1.5-1.1 2.8-1.9 3.9zm2.3-5.9H9.7a14 14 0 0 1 0-4h4.6a14 14 0 0 1 0 4zm.3 5.9a15 15 0 0 0 1.3-3.9h3a8 8 0 0 1-4.3 3.9zm1.7-5.9a16 16 0 0 0 0-4h3.4a8 8 0 0 1 0 4z"/></svg>1.800.555.0147</li>
    <li><svg viewBox="0 0 24 24"><path d="M6.6 10.8a15 15 0 0 0 6.6 6.6l2.2-2.2a1 1 0 0 1 1-.25 11.4 11.4 0 0 0 3.6.57 1 1 0 0 1 1 1V20a1 1 0 0 1-1 1A17 17 0 0 1 3 4a1 1 0 0 1 1-1h3.5a1 1 0 0 1 1 1c0 1.25.2 2.45.57 3.57a1 1 0 0 1-.25 1z"/></svg>780.555.0188</li>
    <li><svg viewBox="0 0 24 24"><path d="M16 1H8a2 2 0 0 0-2 2v18a2 2 0 0 0 2 2h8a2 2 0 0 0 2-2V3a2 2 0 0 0-2-2zm-4 21a1.3 1.3 0 1 1 0-2.6 1.3 1.3 0 0 1 0 2.6zm4-4H8V4h8z"/></svg>780.555.0274</li>
    <li><svg viewBox="0 0 24 24"><path d="M19 8H5a3 3 0 0 0-3 3v6h4v4h12v-4h4v-6a3 3 0 0 0-3-3zm-3 11H8v-5h8zM18 3H6v4h12z"/></svg>780.555.0219</li>
    <li><svg viewBox="0 0 24 24"><path d="M20 4H4a2 2 0 0 0-2 2v12a2 2 0 0 0 2 2h16a2 2 0 0 0 2-2V6a2 2 0 0 0-2-2zm0 4-8 5-8-5V6l8 5 8-5z"/></svg>dalton@brandvexa.example</li>
  </ul>
</section>
<section class="card card-back">
  <div class="back-glow"></div>
  <div class="url-band">www.brandvexa.example</div>
</section>
</body>
</html>
```